Poster of Insipirational Quotes

Attached is a list of leadership quotes from Arlen Drubeck. I would like a poster made, incorporating whatever design elements you like, potentially including Arlen's face, and one or more of the quotes. I intend to print this out in A3 or larger to hang on my wall.

The quotes are:

Being responsible sometimes means pissing people off.

The day soldiers stop bringing you their problems is the day you have stopped leading them.

Don't be buffaloed by experts and elites. Experts often possess more data than judgment. Elites can become so inbred that they produce hemophiliacs who bleed to death as soon as they are nicked by the real world.

Don't be afraid to challenge the pros, even in their own backyard.

Never neglect details. When everyone's mind is dulled or distracted the leader must be doubly vigilant.

You don't know what you can get away with until you try.

Keep looking below surface appearances. Don't shrink from doing so (just) because you might not like what you find.

Organization doesn't really accomplish anything. Plans don't accomplish anything, either. Theories of management don't much matter. Endeavors succeed or fail because of the people involved. Only by attracting the best people will you accomplish great deeds.

Organization charts and fancy titles count for next to nothing.

Never let your ego get so close to your position that when your position goes, your ego goes with it.

Fit no stereotypes. Don't chase the latest management fads. The situation dictates which approach best accomplishes the team's mission.

Perpetual optimism is a force multiplier.

Look for intelligence and judgment, and most critically, a capacity to anticipate, to see around corners. Also look for loyalty, integrity, a high energy drive, a balanced ego, and the drive to get things done.

Great leaders are almost always great simplifiers, who can cut through argument, debate and doubt, to offer a solution everybody can understand.

The commander in the field is always right and the rear echelon is wrong, unless proved otherwise.

Have fun in your command. Don't always run at a breakneck pace. Take leave when you've earned it: Spend time with your families. Corollary: surround yourself with people who take their work seriously, but not themselves, those who work hard and play hard.

Command is lonely.

Leadership is the art of accomplishing more than the science of management
says is possible.
Updates

I need to modify the specification based on the designs that I've seen.

Target Market(s)

Executive Office

Colors

Designer to choose colors to be used in the design.

Requirements
Must have
• Quotes

```html
<!DOCTYPE html>
<html lang="en">
<head>
<meta charset="utf-8">
<title>Leadership Quotes Poster</title>
<link rel="stylesheet" href="https://fonts.googleapis.com/css2?family=Marcellus&display=swap">
<style>
  :root {
    --backdrop: #e8e9ea;
    --paper: #ffffff;
    --ink: #161616;
    --portrait-light: #f4f4f4;
    --portrait-mid: #d9d9d9;
    --portrait-dark: #bdbdbd;
  }
  html, body {
    margin: 0;
    padding: 0;
    width: 1200px;
    height: 923px;
    overflow: hidden;
    background: radial-gradient(ellipse at 50% 50%, #ffffff 0%, #f1f2f3 55%, var(--backdrop) 100%);
  }
  .poster {
    position: absolute;
    left: 333px;
    top: 78px;
    width: 553px;
    height: 779px;
    background: var(--paper);
    overflow: hidden;
    box-shadow: 0 1px 3px rgba(0, 0, 0, 0.15);
  }
  .portrait {
    position: absolute;
    inset: 0;
    width: 100%;
    height: 100%;
  }
  .quotes {
    position: relative;
    margin: 0;
    padding: 33px 0 0;
    list-style: none;
    text-align: center;
    font-family: "Marcellus", "Times New Roman", serif;
    font-size: 11.5px;
    line-height: 12px;
    letter-spacing: 0.8px;
    white-space: nowrap;
    text-transform: uppercase;
    color: var(--ink);
    -webkit-text-stroke: 0.25px var(--ink);
  }
  .quote + .quote {
    margin-top: 13.4px;
  }
</style>
</head>
<body>
  <main class="poster">
    <svg class="portrait" viewBox="0 0 553 779" role="img" aria-label="Faint pencil-sketch portrait of a man in suit and tie behind the quotes">
      <defs>
        <radialGradient id="head-tone" cx="50%" cy="42%" r="45%">
          <stop offset="0" stop-color="var(--portrait-mid)" stop-opacity="0.55"/>
          <stop offset="1" stop-color="var(--portrait-light)" stop-opacity="0"/>
        </radialGradient>
        <linearGradient id="suit-tone" x1="0" y1="0" x2="0" y2="1">
          <stop offset="0" stop-color="var(--portrait-light)" stop-opacity="0"/>
          <stop offset="1" stop-color="var(--portrait-dark)" stop-opacity="0.45"/>
        </linearGradient>
      </defs>
      <rect x="0" y="0" width="553" height="779" fill="url(#head-tone)"/>
      <rect x="0" y="470" width="553" height="309" fill="url(#suit-tone)"/>
    </svg>

    <ol class="quotes">
      <li class="quote">"Being responsible sometimes means pissing people off."</li>
      <li class="quote">"The day soldiers stop bringing you their problems<br>is the day you have stopped leading them."</li>
      <li class="quote">"Don't be buffaloed by experts and elites. Experts often possess<br>more data than judgment. Elites can become so inbred that they<br>produce hemophiliacs who bleed to death<br>as soon as they are nicked by the real world."</li>
      <li class="quote">"Don't be afraid to challenge the pros, even in their own backyard."</li>
      <li class="quote">"Never neglect details. When everyone's mind is dulled or<br>distracted the leader must be doubly vigilant."</li>
      <li class="quote">"You don't know what you can get away with until you try."</li>
      <li class="quote">"Keep looking below surface appearances. Don't shrink from doing<br>so (just) because you might not like what you find."</li>
      <li class="quote">"Organization doesn't really accomplish anything. Plans don't<br>accomplish anything, either. Theories of management don't much<br>matter. Endeavors succeed or fail because of the people involved.<br>Only by attracting the best people will you accomplish great deeds."</li>
      <li class="quote">"Organization charts and fancy titles count for next to nothing."</li>
      <li class="quote">"Never let your ego get so close to your position<br>that when your position goes, your ego goes with it."</li>
      <li class="quote">"Fit no stereotypes. Don't chase the latest management fads.<br>The situation dictates which approach best accomplishes<br>the team's mission."</li>
      <li class="quote">"Perpetual optimism is a force multiplier."</li>
      <li class="quote">"Look for intelligence and judgment, and most critically, a capacity<br>to anticipate, to see around corners. Also look for loyalty,<br>integrity, a high energy drive, a balanced ego,<br>and the drive to get things done."</li>
      <li class="quote">"Great leaders are almost always great simplifiers, who can cut<br>through argument, debate and doubt,<br>to offer a solution everybody can understand."</li>
      <li class="quote">"The commander in the field is always right<br>and the rear echelon is wrong, unless proved otherwise."</li>
      <li class="quote">"Have fun in your command. Don't always run at a breakneck pace.<br>Take leave when you've earned it: spend time with your families.<br>Corollary: surround yourself with people who take their work<br>seriously, but not themselves, those who work hard and play hard."</li>
      <li class="quote">"Command is lonely."</li>
      <li class="quote">"Leadership is the art of accomplishing more<br>than the science of management says is possible."</li>
    </ol>
  </main>
</body>
</html>
```